CuraNex System Web Page Design

This project is to design 6 pages of a web based medical system for clinics, hospitals, drugs suppliers, general items suppliers, insurance company, laboratories and patients (basically all parties which could be involved in).We want the designs of the browser, button, icon and layout are based on Vex, which is user friendly, looks professional, simple and neat but with powerful functions. We have uploaded few pictures of another system, please do not copy its design because this is not what we are looking for, the pictures are for you to know the elements should be included in our pages. CuraNex web-base system, design 6 pages1. Login PageShould include the following elements-company id with input field-login id with input field-password with input field2. Main Page (Navigation page)Should include the following elements-Appointment-Consultation-Patient-Drugs inventory -General supplies inventory -Laboratory-Suppliers-Insurance-Reports 3. Appointment PageShould include all the the elements in the respective pictures plus the followings-Daily View, Weekly View, Monthly View buttons4. Consultation PageShould include all the the elements in the respective picture5. Patient Page5.1 General information Should include all the the elements in the respective picture5.2 medical history/lab reportsShould include all the the elements in the respective picture plus the followings-Notify patient button-Share report button.
Updated on 28 Nov:
Please stop using Ward Keystone in your designs which is not the name of our system. We have just rename our system to CuraNex, please take note.
We need the system to look professional not playful, do not use too many colors and playful icons.
professional users

```html
<!DOCTYPE html>
<html lang="en">
<head>
<meta charset="utf-8">
<title>CuraNex – Appointment</title>
<link rel="stylesheet" href="https://fonts.googleapis.com/css2?family=Roboto:ital,wght@0,300;0,400;0,500;0,700;1,400;1,500&display=swap">
<style>
  :root {
    --brand: #0b6dbd;
    --brand-dark: #095da3;
    --menu-rule: #2b82c9;
    --ink: #3a3a3a;
    --muted: #5a5a5a;
    --placeholder: #b8b8b8;
    --panel: #f2f2f2;
    --panel-edge: #d6d6d6;
    --tab: #e3e3e3;
    --field: #ffffff;
    --field-edge: #c9c9c9;
    --page: #ffffff;
  }
  * { box-sizing: border-box; margin: 0; padding: 0; }
  html, body { width: 1200px; height: 700px; overflow: hidden; background: var(--page); }
  body { font-family: "Roboto", Arial, sans-serif; color: var(--ink); position: relative; }

  .sidebar {
    position: absolute; left: 0; top: 0; width: 202px; height: 700px; background: var(--brand); color: #fff;
  }
  .sidebar-title {
    position: absolute; left: 53px; top: 137px; font-size: 20px; font-style: italic; font-weight: 400; letter-spacing: .3px;
  }
  .menu { position: absolute; left: 0; top: 203px; width: 202px; list-style: none; border-top: 1px solid var(--menu-rule); }
  .menu li {
    height: 32px; line-height: 31px; padding-left: 55px; font-size: 12.5px; font-weight: 500;
    text-transform: uppercase; border-bottom: 1px solid var(--menu-rule); letter-spacing: .2px;
  }
  .menu li.is-active { font-style: italic; }

  .brand-name {
    position: absolute; left: 256px; top: 52px; font-size: 24px; font-weight: 700; color: var(--brand); letter-spacing: -.3px;
  }

  .top-nav { position: absolute; top: 56px; left: 722px; display: flex; align-items: center; font-size: 17px; font-weight: 300; color: var(--muted); }
  .top-nav .nav-item { display: flex; align-items: center; }
  .top-nav .support { margin-right: 30px; }
  .top-nav .support svg { margin-right: 13px; }
  .top-nav .language { margin-right: 25px; }
  .search {
    position: absolute; left: 1044px; top: 59px; width: 131px; height: 21px; border: 1px solid #c4c4c4; border-radius: 11px;
    font-size: 11px; color: var(--placeholder); padding-left: 11px; line-height: 19px;
  }
  .search svg { position: absolute; right: 9px; top: 4px; }

  .page-heading { position: absolute; left: 202px; top: 135px; display: flex; align-items: center; }
  .page-heading .lead-rule { width: 26px; height: 3px; background: var(--brand); margin-right: 5px; }
  .page-heading h1 { font-size: 25px; font-weight: 500; color: var(--brand); letter-spacing: .1px; }
  .page-heading .tail { margin-left: 2px; }

  .tabs { position: absolute; left: 229px; top: 194px; display: flex; gap: 3px; }
  .tab {
    width: 102px; height: 36px; background: var(--tab); border: 1px solid var(--panel-edge); border-bottom: none;
    border-radius: 12px 12px 0 0; font-size: 14px; font-weight: 500; color: #222; text-align: center; line-height: 36px;
  }
  .tab.narrow { font-size: 13px; }
  .tab.is-active { background: var(--panel); color: var(--brand); height: 37px; position: relative; z-index: 2; width: 106px; }

  .panel {
    position: absolute; left: 229px; top: 229px; width: 946px; height: 440px; background: var(--panel); border: 1px solid var(--panel-edge);
  }

  .form-col { position: absolute; top: 24px; display: grid; grid-auto-rows: 31px; }
  .form-col.left { left: 0; grid-template-columns: 161px 250px; }
  .form-col.right { left: 430px; grid-template-columns: 143px 253px; }
  .label { font-size: 14.5px; color: var(--ink); text-align: right; padding-right: 6px; line-height: 31px; }
  .input { align-self: center; height: 22px; background: var(--field); border: 1px solid var(--field-edge); border-radius: 6px;
    font-size: 12px; color: var(--placeholder); padding-left: 6px; line-height: 20px; }
  .label.top { line-height: 20px; padding-top: 5px; }
  .textarea { grid-row: span 4; height: 103px; align-self: start; margin-top: 5px; background: var(--field); border: 1px solid var(--field-edge); border-radius: 6px; }

  .gender { display: flex; align-items: center; font-size: 12px; color: var(--ink); padding-left: 6px; }
  .gender .label-inline { font-size: 14.5px; margin-right: 12px; margin-left: -42px; }
  .radio { width: 12px; height: 12px; border: 1px solid #777; border-radius: 50%; background: #fff; margin-right: 4px; position: relative; }
  .radio.is-checked::after { content: ""; position: absolute; left: 2px; top: 2px; width: 6px; height: 6px; border-radius: 50%; background: #111; }
  .gender .option { display: flex; align-items: center; margin-right: 10px; }

  .actions { position: absolute; left: 93px; top: 377px; display: flex; gap: 18px; }
  .btn {
    width: 108px; height: 33px; background: var(--brand); border-radius: 4px; color: #fff; font-size: 13px; font-weight: 500;
    text-align: center; line-height: 33px;
  }
  .actions .btn:nth-child(2) { margin-left: 1px; }
</style>
</head>
<body>
  <aside class="sidebar">
    <div class="sidebar-title">MENU</div>
    <ul class="menu">
      <li class="is-active">Appointment</li>
      <li>Patient</li>
      <li>Consultation</li>
      <li>Expenses</li>
      <li>Drug Book</li>
      <li>Inventory</li>
      <li>Report</li>
      <li>Configuration</li>
    </ul>
  </aside>

  <div class="brand-name">CuraNex</div>

  <nav class="top-nav">
    <span class="nav-item support">
      <svg width="15" height="15" viewBox="0 0 24 24" aria-hidden="true"><path fill="#111" d="M19.4 13a7.7 7.7 0 0 0 0-2l2.1-1.6-2-3.5-2.5 1a7.4 7.4 0 0 0-1.7-1L15 3h-4l-.4 2.8a7.4 7.4 0 0 0-1.7 1l-2.5-1-2 3.5L6.6 11a7.7 7.7 0 0 0 0 2l-2.1 1.6 2 3.5 2.5-1a7.4 7.4 0 0 0 1.7 1L11 21h4l.4-2.8a7.4 7.4 0 0 0 1.7-1l2.5 1 2-3.5zM13 15.5a3.5 3.5 0 1 1 0-7 3.5 3.5 0 0 1 0 7z" transform="translate(-1 0)"/></svg>
      Support
    </span>
    <span class="nav-item language">Language</span>
    <span class="nav-item">Sign out</span>
  </nav>
  <div class="search">Search
    <svg width="12" height="12" viewBox="0 0 12 12" aria-hidden="true"><circle cx="7" cy="5" r="3.6" fill="none" stroke="#888" stroke-width="1.3"/><line x1="4.4" y1="7.6" x2="1.2" y2="10.8" stroke="#888" stroke-width="1.5"/></svg>
  </div>

  <div class="page-heading">
    <span class="lead-rule"></span>
    <h1>APPOINTMENT</h1>
    <svg class="tail" width="46" height="16" viewBox="0 0 46 16" aria-hidden="true"><line x1="0" y1="8" x2="34" y2="8" stroke="#0b6dbd" stroke-width="3"/><circle cx="38" cy="8" r="5.5" fill="#fff" stroke="#0b6dbd" stroke-width="2.5"/></svg>
  </div>

  <div class="tabs">
    <div class="tab is-active">Register</div>
    <div class="tab">Current</div>
    <div class="tab narrow">Public Holiday</div>
    <div class="tab">Recall</div>
    <div class="tab">Laboratory</div>
    <div class="tab">Reminder</div>
    <div class="tab">Daily View</div>
    <div class="tab">Weekly View</div>
    <div class="tab">Monthly View</div>
  </div>

  <section class="panel">
    <div class="form-col left">
      <span class="label">Patient Code:</span><span class="input"></span>
      <span class="label">English Name:</span><span class="input"></span>
      <span class="label">Chinese Name:</span><span class="input"></span>
      <span class="label">H.K.I.D:</span><span class="input"></span>
      <span class="label">Mobile No.:</span><span class="input"></span>
      <span class="label">Email:</span><span class="input"></span>
      <span class="label">Ocupation:</span><span class="input"></span>
      <span class="label top">Res. Address:</span><span class="textarea"></span>
    </div>

    <div class="form-col right">
      <span class="label">D.O.B:</span><span class="input">DD/MM/CCYY</span>
      <span class="label"></span>
      <span class="gender">
        <span class="label-inline">Gender:</span>
        <span class="option"><span class="radio is-checked"></span>Male</span>
        <span class="option"><span class="radio"></span>Female</span>
      </span>
      <span class="label">Prefix:</span><span class="input"></span>
      <span class="label">Blood Type:</span><span class="input"></span>
      <span class="label">Tel:</span><span class="input"></span>
      <span class="label">Referred by:</span><span class="input"></span>
      <span class="label">Dr. In Charge:</span><span class="input"></span>
      <span class="label top">Bus. Address:</span><span class="textarea"></span>
    </div>

    <div class="actions">
      <span class="btn">New</span>
      <span class="btn">Save</span>
      <span class="btn">Print Eng.</span>
      <span class="btn">Print Chi.</span>
      <span class="btn">Patient Chart</span>
      <span class="btn">Main</span>
    </div>
  </section>
</body>
</html>
```